Vital Spark Electrical in need of a business card design

We need a new business card designed for our electrical business. We have a logo already which I will attach below.
Would like the business card to be..
-BLACK background preferably, possibly white back ground behind logo if colours clash.
-White & Blue (logo blue) text
Something that makes the logo pop, & a modern look. Possibly minimal clean format.

REQUIRE:
-Logo on front & back

TEXT TO INCLUDE (ON ONE SIDE):

Tom Harlow
Director/Electrician
M: 0417 365 208
E:info@vitalsparkelectrical-example.com.au
W:www.vitalsparkelectrical-example.com.au
R.E.C 57318

Custom/New Homes
Renovations
Commercial Office/Shop Fit-outs
Communications & Security Cameras
Electric Vehicle Chargers
Airconditioning
Updates

Requirements
Nice to have
• Possibly even lighten the grey shades for the words 'Vital' & 'Spark' to be more easily read on a black background.

```html
<!DOCTYPE html>
<html lang="en">
<head>
<meta charset="utf-8">
<title>Vital Spark Electrical – Business Card</title>
<link rel="stylesheet" href="https://fonts.googleapis.com/css2?family=Source+Sans+3:wght@400;600&display=swap">
<style>
  :root {
    --backdrop: #555555;
    --card: #131313;
    --blue: #12a5e0;
    --white: #e6e6e6;
    --name-first: #36414b;
    --name-last: #5d6873;
  }
  * { margin: 0; padding: 0; box-sizing: border-box; }
  html, body { width: 1065px; height: 1200px; overflow: hidden; }
  body {
    background: var(--backdrop);
    font-family: "Source Sans 3", "Calibri", sans-serif;
    position: relative;
  }
  .card {
    position: absolute;
    width: 584px;
    height: 363px;
    background: var(--card);
    box-shadow: 3px 4px 6px rgba(0,0,0,0.45);
  }
  .card--front { left: 292px; top: 218px; border-radius: 0 182px 182px 0; }
  .card--back  { left: 263px; top: 623px; border-radius: 182px 0 0 182px; }

  .person { position: absolute; left: 31px; top: 36px; }
  .person__name { font-size: 27px; font-weight: 600; line-height: 1; letter-spacing: -0.3px; }
  .person__first { color: var(--name-first); }
  .person__last { color: var(--name-last); }
  .person__role { color: var(--blue); font-size: 16px; margin-top: 6px; }
  .licence { position: absolute; left: 32px; top: 104px; font-size: 16px; color: var(--white); }
  .licence__label { color: var(--blue); }

  .wordmark {
    position: absolute;
    display: flex;
    align-items: center;
    gap: 12px;
    font-size: 32px;
    font-weight: 600;
    color: var(--blue);
    line-height: 1;
    white-space: nowrap;
  }
  .wordmark__square { width: 16px; height: 16px; background: var(--blue); }
  .card--front .wordmark { left: 186px; top: 166px; }
  .card--back .wordmark { left: 62px; top: 166px; }

  .contacts { position: absolute; left: 32px; top: 258px; list-style: none; }
  .contacts li {
    display: flex; align-items: center; gap: 6px;
    font-size: 16px; color: var(--white); height: 21.5px;
  }
  .contacts svg { width: 15px; height: 15px; flex: none; }
  .contacts .accent { color: var(--blue); }

  .services { position: absolute; right: 30px; list-style: none; text-align: right; }
  .services li {
    font-size: 16px; color: var(--white); height: 26.5px;
    display: flex; justify-content: flex-end; align-items: center; gap: 9px;
  }
  .services li::after {
    content: ""; width: 8px; height: 8px; border-radius: 50%; background: var(--blue); margin-top: 3px;
  }
  .services--top { top: 34px; }
  .services--bottom { top: 251px; }
</style>
</head>
<body>

<section class="card card--front">
  <div class="person">
    <p class="person__name"><span class="person__first">Tom</span> <span class="person__last">Harlow</span></p>
    <p class="person__role">Director/Electrician</p>
  </div>
  <p class="licence"><span class="licence__label">R.E.C</span> 57318</p>

  <div class="wordmark"><span class="wordmark__square"></span>Vital Spark Electrical</div>

  <ul class="contacts">
    <li>
      <svg viewBox="0 0 16 16" fill="none" stroke="#12a5e0" stroke-width="1.6" aria-hidden="true"><path d="M3 2l3 1 1 3-2 1.5c1 2 2 3 4 4L10.5 9.5l3 1 1 3-2 1.5C7 14 2 9 1.5 3.5z"/><path d="M9 1.5a5.5 5.5 0 0 1 5.5 5.5M9 4a3 3 0 0 1 3 3"/></svg>
      0417 365 208
    </li>
    <li>
      <svg viewBox="0 0 16 16" aria-hidden="true"><rect x="0.5" y="3" width="15" height="10" fill="#12a5e0"/><path d="M0.5 3L8 9l7.5-6M0.5 13l5.5-5M15.5 13l-5.5-5" fill="none" stroke="#131313" stroke-width="1.2"/></svg>
      info@vitalsparkelectrical-example.com.au
    </li>
    <li>
      <svg viewBox="0 0 16 16" fill="none" stroke="#12a5e0" stroke-width="1.3" aria-hidden="true"><circle cx="8" cy="8" r="7"/><ellipse cx="8" cy="8" rx="3" ry="7"/><path d="M1 8h14M2 4.5h12M2 11.5h12"/></svg>
      <span>www.<span class="accent">vitalsparkelectrical-example</span>.com.au</span>
    </li>
  </ul>
</section>

<section class="card card--back">
  <ul class="services services--top">
    <li>Custom/New Homes</li>
    <li>Renovations</li>
    <li>Commercial Office/Shop Fit-outs</li>
  </ul>

  <div class="wordmark"><span class="wordmark__square"></span>Vital Spark Electrical</div>

  <ul class="services services--bottom">
    <li>Communications &amp; Security Cameras</li>
    <li>Electric Vehicle Chargers</li>
    <li>Airconditioning</li>
  </ul>
</section>

</body>
</html>
```